Flyer design for the Harvest Lantern Summit 2019 (HALSUM)

Design a flyer for our annual conference with basic information about the conference: conference logo and year, Conference name: Harvest Lantern Summit Location: Talbot Community Center (Downtown Portland)482 Wexley Street, Portland, ME 04109, Date: August 8th, 9th, 10th and 11th, 2019Start time 7:00PMI would like the following three words added to the flyer. These words describe the vision of the conference: Prophetic, Fire, Overflow,

Contact info:
Website: www.vostel.org
Phone: 207 555 3184
Email: contact@meadowcrest.org

Target Market(s)

Young adults living in the United States

Industry/Entity Type

Religious

Font styles to use
Sans Serif

Colors

Designer to choose colors to be used in the design.

Requirements
Must have
• HALSUM must logo standout, the reader should be able to take a quick look and find key info,
Should not have
• Cross image, church image

```html
<!DOCTYPE html>
<html lang="en">
<head>
<meta charset="utf-8">
<title>Harvest Lantern Summit 2019</title>
<link rel="stylesheet" href="https://fonts.googleapis.com/css2?family=Source+Sans+3:wght@400;600&display=swap">
<style>
  :root {
    --navy: #27465a;
    --ink: #2f3b42;
    --title: #34505f;
    --gold: #f6c11d;
    --white: #ffffff;
    --soft: #e8eef1;
  }
  * { margin: 0; padding: 0; box-sizing: border-box; }
  html, body { width: 857px; height: 1200px; overflow: hidden; background: var(--white); }
  body { font-family: "Source Sans 3", "Segoe UI", sans-serif; }
  .flyer { position: relative; width: 857px; height: 1200px; overflow: hidden; }
  .hero-photo {
    position: absolute; left: 0; top: 0; width: 857px; height: 540px;
    background: linear-gradient(160deg, #c9b36a 0%, #8f8a4c 35%, #d8c27a 60%, #6f7a3e 100%);
  }
  .shapes { position: absolute; left: 0; top: 0; }
  .title {
    position: absolute; left: 89px; top: 432px;
    font-size: 34px; line-height: 49px; font-weight: 400; color: var(--title);
  }
  .vision-word {
    position: absolute; width: 258px; text-align: center;
    font-size: 36px; color: var(--ink); transform: rotate(16.7deg); transform-origin: center;
  }
  .event-mark {
    position: absolute; left: 87px; top: 990px; width: 240px; text-align: center;
    font-size: 38px; font-weight: 600; color: var(--title); letter-spacing: 1px; line-height: 48px;
  }
  .info-block { position: absolute; left: 511px; color: var(--white); }
  .info-label { font-size: 24px; font-weight: 400; letter-spacing: 0.5px; margin-bottom: 6px; }
  .info-text { font-size: 21px; line-height: 29px; color: var(--soft); }
  .contact-item {
    position: absolute; top: 1133px;
    font-size: 17px; line-height: 24px; color: var(--ink);
  }
</style>
</head>
<body>
<main class="flyer">
  <div class="hero-photo" role="img" aria-label="Photo of a smiling family of parents and four young daughters hugging outdoors on sunny grass"></div>

  <svg class="shapes" width="857" height="1200" viewBox="0 0 857 1200" aria-hidden="true">
    <polygon points="0,300 428,458 428,1103 0,1103" fill="var(--white)"/>
    <polygon points="87,330 428,425 428,462 87,360" fill="var(--gold)"/>
    <polygon points="428,401 857,527 857,1103 428,1103" fill="var(--navy)"/>
    <polygon points="87,604 345,681 345,763 87,686" fill="var(--gold)"/>
    <polygon points="87,701 345,778 345,860 87,783" fill="var(--gold)"/>
    <polygon points="87,798 345,875 345,957 87,880" fill="var(--gold)"/>
    <rect x="0" y="1103" width="857" height="97" fill="var(--gold)"/>
    <circle cx="428" cy="643" r="37" fill="var(--gold)"/>
    <path d="M428 666 C418 652 412 643 412 634 A16 16 0 0 1 444 634 C444 643 438 652 428 666 Z" fill="none" stroke="var(--white)" stroke-width="2.5"/>
    <circle cx="428" cy="634" r="6" fill="none" stroke="var(--white)" stroke-width="2.5"/>
    <circle cx="428" cy="882" r="37" fill="var(--gold)"/>
    <path d="M445 876 A18 18 0 1 1 438 867" fill="none" stroke="var(--white)" stroke-width="2.5"/>
    <path d="M428 870 L428 883 L436 890" fill="none" stroke="var(--white)" stroke-width="2.5"/>
    <rect x="87" y="1137" width="34" height="22" fill="none" stroke="var(--ink)" stroke-width="2.5"/>
    <path d="M87 1137 L104 1151 L121 1137 M87 1159 L100 1148 M121 1159 L108 1148" fill="none" stroke="var(--ink)" stroke-width="2"/>
    <path d="M408 1134 q4 -3 7 1 l4 6 q2 3 -1 6 l-3 2 q3 7 10 11 l2 -3 q3 -3 6 -1 l6 4 q4 3 1 7 l-3 3 q-6 4 -18 -5 q-12 -10 -14 -22 q0 -6 3 -9 z" fill="var(--ink)"/>
    <circle cx="637" cy="1148" r="11" fill="var(--ink)"/>
    <path d="M630 1141 q4 2 3 6 q3 2 2 6 M640 1140 q-2 4 3 6 q4 -1 5 3" fill="none" stroke="var(--gold)" stroke-width="2"/>
  </svg>

  <h1 class="title">Harvest<br>Lantern<br>Summit</h1>

  <div class="vision-word" style="left:87px; top:659px;">Prophetic</div>
  <div class="vision-word" style="left:87px; top:756px;">Fire</div>
  <div class="vision-word" style="left:87px; top:853px;">Overflow</div>

  <div class="event-mark">HALSUM 2019</div>

  <section class="info-block" style="top:598px;">
    <h2 class="info-label">LOCATION</h2>
    <p class="info-text">Talbot Community Center<br>(Downtown Portland)<br>482 Wexley Street,<br>Portland, ME 04109</p>
  </section>

  <section class="info-block" style="top:843px;">
    <h2 class="info-label">DATE</h2>
    <p class="info-text">August 8th, 9th, 10th and<br>11th, 2019<br>Start time 7:00PM</p>
  </section>

  <div class="contact-item" style="left:135px;">contact@meadowcrest.org</div>
  <div class="contact-item" style="left:451px;">207 555 3184</div>
  <div class="contact-item" style="left:661px;">www.vostel.org</div>
</main>
</body>
</html>
```